New Packaging Design Project

Wine packaging redesign. Retail partner requested a redesign of a private label wine. The old label is attached. Our partner liked the Lantern and Briar label and wanted something similar. There will be a logo added to the top of the label

Went on vacation/holiday

```html
<!DOCTYPE html>
<html lang="en">
<head>
<meta charset="utf-8">
<title>Napa Valley Red Blend – Wine Label</title>
<link rel="stylesheet" href="https://fonts.googleapis.com/css2?family=Oranienbaum&family=Cinzel:wght@600&family=Josefin+Sans:wght@300&display=swap">
<style>
  :root {
    --paper: #ffffff;
    --slate: #3a3a3a;
    --slate-dark: #2c2c2c;
    --silver-light: #f2f2f2;
    --silver-mid: #b9b9b9;
    --silver-dark: #7d7d7d;
    --ink-light: #e6e6e6;
    --ribbon-red: #d3232b;
  }
  html, body {
    margin: 0;
    padding: 0;
    width: 823px;
    height: 1200px;
    overflow: hidden;
    background: var(--paper);
  }
  .canvas {
    position: relative;
    width: 823px;
    height: 1200px;
    background: var(--paper);
  }
  .label {
    position: absolute;
    left: 36px;
    top: 36px;
    width: 752px;
    height: 1128px;
    background: radial-gradient(ellipse at 50% 45%, var(--slate) 0%, var(--slate-dark) 100%);
    overflow: hidden;
  }
  .ornament-band {
    position: absolute;
    left: 0;
    width: 100%;
    height: 155px;
    background: linear-gradient(90deg, #6e6e6e 0%, #9a9a9a 30%, #868686 60%, #a3a3a3 100%);
  }
  .ornament-band--top { top: 0; }
  .ornament-band--bottom { bottom: 0; }
  .silver-rule {
    position: absolute;
    left: 0;
    width: 100%;
    height: 15px;
    background: linear-gradient(90deg, var(--silver-dark) 0%, var(--silver-light) 40%, var(--silver-mid) 70%, var(--silver-dark) 100%);
  }
  .silver-rule--top { top: 158px; }
  .silver-rule--bottom { top: 956px; }
  .vine-illustration {
    position: absolute;
    left: 123px;
    top: 192px;
    width: 516px;
    height: 362px;
    border-radius: 8px;
    background: radial-gradient(ellipse at 50% 45%, rgba(230,230,230,0.22) 0%, rgba(230,230,230,0.08) 55%, rgba(230,230,230,0) 80%);
  }
  .region-title {
    position: absolute;
    left: 0;
    top: 608px;
    width: 100%;
    margin: 0;
    text-align: center;
    font-family: "Oranienbaum", "Times New Roman", serif;
    font-weight: 400;
    font-size: 104px;
    line-height: 1;
    letter-spacing: 7px;
    color: var(--silver-mid);
    background: linear-gradient(90deg, #8a8a8a 0%, #f0f0f0 30%, #a8a8a8 55%, #e8e8e8 80%, #9a9a9a 100%);
    -webkit-background-clip: text;
    background-clip: text;
    -webkit-text-fill-color: transparent;
    transform: scaleX(0.86);
  }
  .wine-style {
    position: absolute;
    left: 0;
    top: 772px;
    width: 100%;
    display: flex;
    justify-content: center;
    align-items: center;
    gap: 10px;
  }
  .wine-style__ribbon { display: block; }
  .wine-style__name {
    font-family: "Cinzel", "Times New Roman", serif;
    font-weight: 600;
    font-size: 28px;
    letter-spacing: 3px;
    color: var(--silver-light);
    line-height: 1;
  }
  .varietals {
    position: absolute;
    left: 0;
    top: 844px;
    width: 100%;
    margin: 0;
    text-align: center;
    font-family: "Josefin Sans", "Helvetica", sans-serif;
    font-weight: 300;
    font-size: 20px;
    line-height: 39px;
    color: var(--ink-light);
  }
  .varietals .sep { margin: 0 10px; }
</style>
</head>
<body>
<div class="canvas">
  <div class="label">
    <div class="ornament-band ornament-band--top" role="img" aria-label="Engraved silver pattern of grape vines, leaves and clusters"></div>
    <div class="silver-rule silver-rule--top"></div>

    <div class="vine-illustration" role="img" aria-label="Chalk-line sketch of a grapevine on a trellis with hanging grape clusters"></div>

    <h1 class="region-title">NAPA VALLEY</h1>

    <div class="wine-style">
      <svg class="wine-style__ribbon" width="40" height="30" viewBox="0 0 40 30" aria-hidden="true">
        <polygon points="0,0 40,0 40,30 0,30 10,15" fill="var(--ribbon-red)"/>
      </svg>
      <span class="wine-style__name">RED BLEND</span>
      <svg class="wine-style__ribbon" width="40" height="30" viewBox="0 0 40 30" aria-hidden="true">
        <polygon points="0,0 40,0 30,15 40,30 0,30" fill="var(--ribbon-red)"/>
      </svg>
    </div>

    <p class="varietals">
      MERLOT<span class="sep">|</span>CABERNET SAUVIGNON<br>
      CABERNET FRANC<span class="sep">|</span>PETIT VERDOT<span class="sep">|</span>MALBEC
    </p>

    <div class="silver-rule silver-rule--bottom"></div>
    <div class="ornament-band ornament-band--bottom" role="img" aria-label="Engraved silver pattern of grape vines, leaves and clusters"></div>
  </div>
</div>
</body>
</html>
```